web page template design

We'd like to see a few designs based on the selected logo. See attached color logo.

We'll need a homepage design which will display the competition announcement and limited details about it. There will be links (or tabs) to the follow on pages which will contain all of the legal details, sign-up and design submission page, finalist selection page, winner announcement page, jury (judges) background page, company sponsor (Verant) details, press release page and a blog page. These are just guidelines for the number of subpage links.

So we'd like a primary page and a follow-on page which is a little more plain.

Here is the competition briefer below:

In January 2014, Verant Tile Inc. will launch its 1st Annual Verant Tile Floor Design Competition. This design competition will be open to Design and Architecture students of the NYC area. Students and student groups can submit cork flooring design concepts online to a judging committee of prominent designers and architects who will select design finalists and a winner. The winning design will highlight the unique creative possibilities of sustainable cork tiles. The winner will receive a cash prize and publication of their winning design through press releases and various media outlets as well as on the PlankMosaic.example website. The winning floor will be created and photographed by Verant Tile and will be donated to a deserving non-profit community center in NYC. The donated cork floor will be installed at no cost to the non-profit community center.

Target Market(s)

designers and architects.

Industry/Entity Type

Non-Profit

Requirements
Must have
• tabs or link system

```html
<!DOCTYPE html>
<html lang="en">
<head>
<meta charset="utf-8">
<title>Verant Tile Floor Design Competition 2014</title>
<link rel="stylesheet" href="https://fonts.googleapis.com/css2?family=Exo+2:wght@300;400&family=Open+Sans:wght@400;600;700&display=swap">
<style>
:root{
  --red:#c6473b;--gold:#d4a027;--yellow:#f8cb50;--sage:#d8d88c;--teal:#5eaeb9;
  --ink:#3a3a3a;--muted:#8a8a8a;--nav-text:#b07d24;--panel:#e5e5ea;
  --footer:#141414;--footer-base:#1e1e1e;--band:#d6d6d6;--paper:#f8f9f8;
}
*{box-sizing:border-box;margin:0;padding:0}
html,body{width:1029px;height:1200px;overflow:hidden;background:#fff}
body{font-family:"Open Sans",Arial,sans-serif;color:var(--ink)}
.page{position:absolute;left:0;top:0;width:1200px;height:1400px;transform:scale(.8575);transform-origin:0 0}
.abs{position:absolute}
.stripe{left:180px;width:838px;display:flex}
.stripe span{flex:1 1 0}
.stripe .s1{background:var(--red)}.stripe .s2{background:var(--gold)}.stripe .s3{background:var(--yellow)}.stripe .s4{background:var(--sage)}.stripe .s5{background:var(--teal)}
.header{left:180px;top:5px;width:838px;height:93px;background:var(--paper)}
.toplinks{left:166px;top:76px;font-size:7px;letter-spacing:.4px;color:#555;display:flex;gap:14px}
.register{right:168px;top:76px;font-size:7px;letter-spacing:.4px;color:#555}
.register u{color:#444}
.brand{left:358px;top:11px;width:122px;height:82px;background:#f1f2f0;text-align:center}
.brand-dot{width:34px;height:34px;border-radius:50%;background:var(--gold);margin:4px auto 5px}
.brand-name{font-size:10px;font-weight:700;color:#2c2c2c;line-height:10px}
.brand-sub{font-size:6px;letter-spacing:2.4px;color:#2c2c2c;line-height:9px}
.brand-year{font-size:7px;font-weight:700;color:var(--red);line-height:8px}
.nav{left:180px;top:98px;width:838px;height:32px;background:var(--yellow)}
.nav ul{list-style:none;display:flex;position:absolute;left:165px;top:12px;font-size:7px;font-weight:600;letter-spacing:.3px;color:var(--nav-text)}
.nav li{margin-right:30px}
.nav .login-label{position:absolute;right:207px;top:12px;font-size:7px;font-weight:600;color:#c9963a}
.nav .user{position:absolute;left:639px;top:0;width:32px;height:32px;background:var(--gold)}
.hero{left:180px;top:130px;width:838px;height:282px;background:radial-gradient(ellipse at 30% 100%,#8a5a37 0%,transparent 55%),linear-gradient(180deg,#6d5a4c 0%,#8e7a66 35%,#9b7152 65%,#b7875f 100%)}
.hero-date{left:171px;top:49px;width:86px;height:16px;background:var(--teal);color:#fff;font-size:6px;font-weight:700;letter-spacing:.4px;padding:4px 0 0 18px;white-space:nowrap}
.hero-title{left:166px;top:72px;width:360px;font-family:"Exo 2",sans-serif;font-weight:300;font-size:31px;line-height:38px;color:var(--yellow)}
.hero-copy{left:169px;top:160px;width:400px;font-size:9px;line-height:13px;color:#f3ece4}
.hero-btn{left:170px;top:219px;width:74px;height:30px;border:1px solid #eee;color:#fff;font-size:6.5px;font-weight:700;text-align:center;line-height:28px;letter-spacing:.3px}
.login{left:678px;top:130px;width:173px;height:108px;background:var(--gold)}
.login .field{position:absolute;left:12px;width:149px;height:20px;background:#e7e7ee;font-size:7px;color:#777;padding:6px 7px}
.login .btn{position:absolute;left:12px;top:72px;width:55px;height:21px;background:var(--yellow);color:var(--red);font-size:7px;font-weight:700;text-align:center;line-height:21px}
.login .lost{position:absolute;left:83px;top:79px;font-size:7px;font-weight:600;color:#fff}
.post{left:353px;top:434px;width:322px;height:269px;background:var(--panel)}
.post-photo{left:0;top:0;width:322px;height:157px;background:linear-gradient(180deg,#7fa3c8 0%,#a6b7c6 45%,#6c5f4f 70%,#2f5d80 82%,#325f82 100%)}
.post-date{left:0;top:0;width:89px;height:20px;background:var(--teal);color:#fff;font-size:7px;padding:6px 0 0 7px;white-space:nowrap}
.post-date i{position:absolute;left:70px;top:0;width:19px;height:20px;background:#4d9aa4}
.post h2{position:absolute;left:17px;top:172px;font-family:"Exo 2",sans-serif;font-weight:300;font-size:19px;color:#666}
.post p{position:absolute;left:17px;top:205px;width:290px;font-size:7.5px;line-height:11.5px;color:#777}
.post .more{position:absolute;left:244px;top:248px;font-size:7.5px;font-weight:700;color:var(--gold)}
.blog{left:686px;top:425px;width:159px;height:278px;background:#fff;box-shadow:0 0 4px rgba(0,0,0,.08)}
.blog h3{position:absolute;left:11px;top:9px;font-size:12px;font-weight:600;color:#333}
.blog .rule{position:absolute;left:0;top:32px;width:159px;height:1px;background:#e6e6e6}
.blog-item{position:absolute;left:10px;width:140px;height:40px}
.blog-item .thumb{position:absolute;left:0;top:0;width:37px;height:37px}
.blog-item .t{position:absolute;left:46px;top:0;font-size:7px;font-weight:600;line-height:10.5px;color:#333;width:92px}
.blog-item .ago{position:absolute;left:46px;top:27px;font-size:6.5px;color:#aaa}
.finalists{left:180px;top:726px;width:838px;height:234px;background:var(--teal)}
.sec-title{font-size:12px;color:#fff;display:flex;align-items:center;gap:5px}
.finalist{position:absolute;top:46px;width:113px;text-align:center}
.finalist .photo{width:113px;height:113px}
.finalist .name{margin-top:10px;font-size:8px;font-weight:700;letter-spacing:.6px;color:#fff;white-space:nowrap}
.finalist .bio{margin-top:4px;font-size:5.5px;line-height:9.5px;color:#d9eef1}
.about-title,.jury-title{font-size:12px;color:#666;display:flex;align-items:center;gap:5px}
.about-photo{left:352px;top:1010px;width:78px;height:74px;background:linear-gradient(135deg,#cfd4d8,#8b8f92 50%,#d8d2c8)}
.about-copy{left:440px;top:1010px;width:194px;font-size:6.5px;line-height:8.5px;color:#777}
.about-copy p+p{margin-top:5px}
.about-copy .link{margin-top:11px;font-size:5px;font-weight:700;color:var(--red);text-decoration:underline}
.jury-photo{position:absolute;top:1010px;width:46px;height:46px}
.partners{left:180px;top:1114px;width:838px;height:55px;background:var(--band)}
.partners span{position:absolute;top:19px;font-size:13px;font-weight:600;color:#9a9a9a;white-space:nowrap}
.footer{left:180px;top:1177px;width:838px;height:176px;background:var(--footer);color:#ccc}
.footer h4{position:absolute;top:29px;font-size:9.5px;font-weight:400;color:#fff}
.footer .txt{position:absolute;font-size:6.5px;line-height:10.5px;color:#bbb}
.footer .teal{color:var(--teal)}
.foot-brand{left:174px;top:32px;width:78px;text-align:center}
.foot-brand .dot{width:22px;height:22px;border-radius:50%;background:#e8e8e8;margin:0 auto 3px}
.foot-brand .n{font-size:6px;font-weight:700;color:#fff;white-space:nowrap}
.foot-brand .s{font-size:3.5px;letter-spacing:1.5px;color:#fff;white-space:nowrap}
.email{position:absolute;left:551px;top:91px;width:84px;height:17px;background:#2c2c2c;font-size:6.5px;color:#bbb;padding:4px 8px}
.go{position:absolute;left:635px;top:91px;width:21px;height:17px;background:var(--teal);color:#fff;font-size:6.5px;text-align:center;line-height:17px}
.base{left:180px;top:1353px;width:838px;height:47px;background:var(--footer-base)}
.base .copy{position:absolute;left:175px;top:18px;font-size:7px;color:#bbb}
.social{position:absolute;top:16px;width:14px;height:14px;border-radius:50%}
</style>
</head>
<body>
<div class="page">
  <div class="abs stripe" style="top:0;height:5px"><span class="s1"></span><span class="s2"></span><span class="s3"></span><span class="s4"></span><span class="s5"></span></div>

  <header class="abs header">
    <nav class="abs toplinks"><span>ANNOUNCEMENTS</span><span>PRESS</span><span>BLOG</span></nav>
    <div class="abs brand">
      <div class="brand-dot"></div>
      <div class="brand-name">VERANT TILE FLOOR</div>
      <div class="brand-sub">DESIGN COMPETITION</div>
      <div class="brand-year">2014</div>
    </div>
    <div class="abs register">NO ACCOUNT YET? <u>REGISTER</u></div>
  </header>

  <div class="abs nav">
    <ul><li>HOME</li><li>FINALISTS</li><li>JURY</li><li>SPONSORS</li><li>ABOUT</li><li>CONTACT</li></ul>
    <span class="login-label">USER LOGIN</span>
    <div class="user">
      <svg width="32" height="32" viewBox="0 0 32 32"><circle cx="16" cy="12" r="4" fill="#fff"/><path d="M10 21c0-4 3-5 6-5s6 1 6 5z" fill="#fff"/></svg>
    </div>
  </div>

  <section class="abs hero" role="img" aria-label="Blurred photo of a warm wooden floor">
    <div class="abs hero-date">NOVEMBER 2013</div>
    <h1 class="abs hero-title">1st Annual Verant Tile Design Competition</h1>
    <p class="abs hero-copy">In January 2014, Verant Tile Inc. will launch its 1st Annual Verant Tile Floor Design Competition. This design competition will be open to Design and Architecture students of the NYC area. Students and student groups can submit cork flooring design concepts...</p>
    <div class="abs hero-btn">READ MORE</div>
  </section>

  <form class="abs login">
    <div class="field" style="top:11px">Username</div>
    <div class="field" style="top:42px">Password</div>
    <div class="btn">LOGIN</div>
    <span class="lost">LOST PASSWORD?</span>
  </form>

  <article class="abs post">
    <div class="abs post-photo" role="img" aria-label="City skyline across the water at dusk"></div>
    <div class="abs post-date">08 APRIL, 2013<i></i></div>
    <h2>WHAT IS LOREM IPSUM?</h2>
    <p>Lorem Ipsum is simply dummy text of the printing and typesetting industry. Lorem Ipsum has been the industry's standard dummy text ever since the 1500s, when an unknown printer took a galley of type and..</p>
    <span class="more">READ MORE ›</span>
  </article>

  <aside class="abs blog">
    <h3>Latest from Blog</h3>
    <div class="rule"></div>
    <div class="blog-item" style="top:42px"><div class="thumb" role="img" aria-label="Portrait photo" style="background:#b9aca0"></div><div class="t">A New Yorker doesn't necessarily come from...</div><div class="ago">3 minutes ago</div></div>
    <div class="blog-item" style="top:89px"><div class="thumb" role="img" aria-label="Photo of a hand with a drink" style="background:#d7a79a"></div><div class="t">A New Yorker never looks up...</div><div class="ago">7 hours ago</div></div>
    <div class="blog-item" style="top:136px"><div class="thumb" role="img" aria-label="City skyline photo" style="background:#7b8aa0"></div><div class="t">A New Yorker doesn't take cabs</div><div class="ago">23 hours ago</div></div>
    <div class="blog-item" style="top:182px"><div class="thumb" role="img" aria-label="Cork texture photo" style="background:#c9a47a"></div><div class="t">A New Yorker views celebrities as regular...</div><div class="ago">1 day ago</div></div>
    <div class="blog-item" style="top:229px"><div class="thumb" role="img" aria-label="Wooden floor photo" style="background:#7a3f2a"></div><div class="t">A New Yorker never looks up...</div><div class="ago">2 days ago</div></div>
  </aside>

  <section class="abs finalists">
    <div class="abs sec-title" style="left:174px;top:20px">
      <svg width="11" height="11" viewBox="0 0 12 12"><path d="M3 1h6v3a3 3 0 0 1-6 0zM1 2h2v2H1zM9 2h2v2H9zM5 7h2v2H5zM3 10h6v1H3z" fill="#fff"/></svg>Finalists
    </div>
    <div class="finalist" style="left:173px"><div class="photo" role="img" aria-label="Finalist portrait" style="background:#c9c2bb"></div><div class="name">ARON PELL, NYC</div><div class="bio">Lorem ipsum dolor sit amet, consectetur adipisicing elit, sed do eiusmod tempor incididunt ut labore et dolore magna</div></div>
    <div class="finalist" style="left:298px"><div class="photo" role="img" aria-label="Finalist portrait" style="background:#6a4a3c"></div><div class="name">MIRA VANCE, NYC</div><div class="bio">Lorem ipsum dolor sit amet, consectetur adipisicing elit, sed do eiusmod tempor incididunt ut labore et dolore magna</div></div>
    <div class="finalist" style="left:423px"><div class="photo" role="img" aria-label="Finalist portrait" style="background:#c8b6a6"></div><div class="name">TEO MARLOW, NYC</div><div class="bio">Lorem ipsum dolor sit amet, consectetur adipisicing elit, sed do eiusmod tempor incididunt ut labore et dolore magna</div></div>
    <div class="finalist" style="left:548px"><div class="photo" role="img" aria-label="Finalist portrait" style="background:#7c6d64"></div><div class="name">DANA WHITLOCK, NYC</div><div class="bio">Lorem ipsum dolor sit amet, consectetur adipisicing elit, sed do eiusmod tempor incididunt ut labore et dolore magna</div></div>
  </section>

  <div class="abs about-title" style="left:355px;top:988px">
    <svg width="11" height="11" viewBox="0 0 12 12"><path d="M3 1h6v3a3 3 0 0 1-6 0zM1 2h2v2H1zM9 2h2v2H9zM5 7h2v2H5zM3 10h6v1H3z" fill="var(--teal)"/></svg>About Verant Tile Floor
  </div>
  <div class="abs about-photo" role="img" aria-label="Team working around a table"></div>
  <div class="abs about-copy">
    <p>Lorem ipsum dolor sit amet, consectetur adipisicing elit, sed do eiusmod tempor incididunt ut labore et dolore magna aliqua.</p>
    <p>Ut enim ad minim veniam, quis nostrud exercitation ullamco laboris nisi ut aliquip ex ea commodo consequat.</p>
    <p class="link">READ MORE</p>
  </div>

  <div class="abs jury-title" style="left:647px;top:988px">
    <svg width="11" height="11" viewBox="0 0 12 12"><path d="M3 1h6v3a3 3 0 0 1-6 0zM1 2h2v2H1zM9 2h2v2H9zM5 7h2v2H5zM3 10h6v1H3z" fill="var(--teal)"/></svg>The Jury
  </div>
  <div class="jury-photo" role="img" aria-label="Jury member portrait" style="left:647px;background:#c9c2bb"></div>
  <div class="jury-photo" role="img" aria-label="Jury member portrait" style="left:697px;background:#6a4a3c"></div>
  <div class="jury-photo" role="img" aria-label="Jury member portrait" style="left:748px;background:#c8b6a6"></div>
  <div class="jury-photo" role="img" aria-label="Jury member portrait" style="left:799px;background:#7c6d64"></div>

  <div class="abs partners">
    <span style="left:168px">Norvale</span>
    <span style="left:230px">Brightquay CRM</span>
    <span style="left:335px">Tessaro</span>
    <span style="left:418px">Quilmark</span>
    <span style="left:518px">Harrowline</span>
    <span style="left:616px">Lumeno</span>
  </div>

  <div class="abs stripe" style="top:1169px;height:8px"><span class="s1"></span><span class="s2"></span><span class="s3"></span><span class="s4"></span><span class="s5"></span></div>

  <footer class="abs footer">
    <div class="abs foot-brand"><div class="dot"></div><div class="n">VERANT TILE FLOOR</div><div class="s">DESIGN COMPETITION</div></div>

    <h4 style="left:288px">CONTACT</h4>
    <div class="txt" style="left:288px;top:52px;width:110px">There are many variations of passages of Lorem Ipsum available, but the majority have suf-</div>
    <svg class="abs" style="left:290px;top:91px" width="8" height="10" viewBox="0 0 8 10"><path d="M4 0a3.5 3.5 0 0 1 3.5 3.5C7.5 6 4 10 4 10S.5 6 .5 3.5A3.5 3.5 0 0 1 4 0z" fill="var(--teal)"/><circle cx="4" cy="3.5" r="1.3" fill="#141414"/></svg>
    <div class="txt" style="left:308px;top:92px;color:#fff">Riverside Ave</div>
    <svg class="abs" style="left:289px;top:109px" width="10" height="7" viewBox="0 0 10 7"><rect width="10" height="7" fill="var(--teal)"/><path d="M0 0l5 4 5-4" stroke="#141414" fill="none"/></svg>
    <div class="txt" style="left:308px;top:107px;color:#fff">info@plankmosaic.example</div>
    <svg class="abs" style="left:289px;top:123px" width="9" height="9" viewBox="0 0 9 9"><path d="M1 1l2-1 1 2.5-1 .8a5 5 0 0 0 2.7 2.7l.8-1L9 6 8 8C4 8 1 5 1 1z" fill="var(--teal)"/></svg>
    <div class="txt" style="left:308px;top:123px;color:#fff">555-0100-2040</div>

    <h4 style="left:413px">LATEST TWEETS</h4>
    <svg class="abs" style="left:417px;top:55px" width="10" height="9" viewBox="0 0 10 9"><rect x="0" y="0" width="10" height="6.5" rx="1.5" fill="var(--teal)"/><path d="M2 6.5v2.5l3-2.5z" fill="var(--teal)"/></svg>
    <div class="txt" style="left:434px;top:52px;width:108px">Lorem Ipsum is simply dummy text of the printing and typesetting industry. Lorem Ipsum has<br><span class="teal">1 Hour Ago</span></div>
    <svg class="abs" style="left:417px;top:113px" width="10" height="9" viewBox="0 0 10 9"><rect x="0" y="0" width="10" height="6.5" rx="1.5" fill="var(--teal)"/><path d="M2 6.5v2.5l3-2.5z" fill="var(--teal)"/></svg>
    <div class="txt" style="left:434px;top:110px;width:108px">Lorem Ipsum is simply dummy text of the printing and typeset-<br><span class="teal">1 Hour Ago</span></div>

    <h4 style="left:551px">NEWS LETTER</h4>
    <div class="txt" style="left:551px;top:52px;width:110px">Type your email address below and recive our daily news letter for free</div>
    <div class="email">Email Address</div>
    <div class="go">GO</div>
  </footer>

  <div class="abs base">
    <span class="copy">© 2013 All rights reserved.&nbsp; Verant Tile Floor</span>
    <span class="social" style="left:612px;background:var(--teal)"></span>
    <span class="social" style="left:631px;background:#e8e8e8"></span>
    <span class="social" style="left:650px;background:#e8e8e8"></span>
  </div>
</div>
</body>
</html>
```